Need a new company business card

I am looking for a new company business card. Front and back. With information on it as per below. Card should be professional. Yet clever. Simple. Modern design. ZEP card, traditional size. OK with say, all black or all red backside.

Vornadel is an indie, bootstrapped magazine advancing the work of intersectional feminists busting their buts to create a just world through the power of enterprise and innovation.

Vornadel is the home and voice of entrepreneurial feminism and feminist innovators worldwide. Entrepreneurial feminists are people (of all genders) who see inequality as an innovation priority. They work to advance gender equity and/or who strive to integrate and practice feminist principles, pedagogy, values into their innovation and entrepreneurship work.
We are committed to this space being trans and queer inclusive, anti-racist, intersectional, brave, and safe. We welcome all allies. We value learning, edgy but civil discourse and integrative thinking skills.

Target Market(s)

feminists, business owners,

Industry/Entity Type

Publishing Company

Contact Information for Business Card

TJ Harlow
Founder/Publisher
4-237 Pellridge Street, Toronto, ON
M4T 2K8
publisher@vornadel-example.com
416-555-3042
www.vornadel-example.com

Font styles to use
Serif
Other font styles liked:
• Myriad Pro

Colors
ec1f27
000000
ffffff

Requirements
Must have
• logo
• use red, black white colours only.
Nice to have
• use the compass in pattern or creatively but not too busy please
Should not have
• Should not be too busy. Elegant.

```html
<!DOCTYPE html>
<html lang="en">
<head>
<meta charset="utf-8">
<title>Vornadel Business Card</title>
<link rel="stylesheet" href="https://fonts.googleapis.com/css2?family=Roboto:wght@400;500;700&display=swap">
<style>
  :root {
    --backdrop: #b9b9b9;
    --card-black: #141414;
    --pattern-black: #1c1c1c;
    --card-white: #f7f7f7;
    --brand-red: #d42320;
    --ink: #2b2b2b;
  }
  * { margin: 0; padding: 0; box-sizing: border-box; }
  html, body {
    width: 1200px;
    height: 1138px;
    overflow: hidden;
    background: var(--backdrop);
    font-family: "Roboto", Arial, sans-serif;
  }
  .card {
    position: absolute;
    width: 620px;
    height: 374px;
    border-radius: 16px;
    overflow: hidden;
  }
  .card-back {
    left: 274px;
    top: 186px;
    background: linear-gradient(90deg, var(--card-black), var(--pattern-black));
  }
  .card-front {
    left: 276px;
    top: 608px;
    background: var(--card-white);
    color: var(--ink);
  }
  .brand-name {
    position: absolute;
    left: 72px;
    top: 152px;
    width: 190px;
    text-align: center;
    font-size: 34px;
    font-weight: 700;
    color: var(--brand-red);
  }
  .person {
    position: absolute;
    left: 336px;
    top: 106px;
  }
  .person-name {
    font-size: 22px;
    font-weight: 700;
    color: var(--ink);
  }
  .person-title {
    margin-top: 6px;
    font-size: 15px;
    color: var(--brand-red);
  }
  .contact-list {
    position: absolute;
    left: 336px;
    top: 179px;
    list-style: none;
  }
  .contact-list li {
    display: flex;
    align-items: center;
    height: 20px;
    font-size: 15px;
    color: var(--ink);
  }
  .contact-list svg {
    width: 12px;
    height: 12px;
    margin-right: 12px;
    fill: var(--brand-red);
  }
  .address {
    position: absolute;
    left: 0;
    right: 0;
    bottom: 16px;
    text-align: center;
    font-size: 14.5px;
    color: var(--ink);
  }
</style>
</head>
<body>
  <div class="card card-back" role="img" aria-label="Black card back with a subtle tone-on-tone repeating brand pattern"></div>

  <div class="card card-front">
    <div class="brand-name">Vornadel</div>

    <div class="person">
      <div class="person-name">TJ Harlow</div>
      <div class="person-title">Founder/Publisher</div>
    </div>

    <ul class="contact-list">
      <li>
        <svg viewBox="0 0 12 12" aria-hidden="true"><path d="M1 3c0-1 1-2 5-2s5 1 5 2v1H8V3H4v1H1zM2 5h8l1 6H1zM6 6.5a2 2 0 1 0 0 4 2 2 0 0 0 0-4z"/></svg>
        416-555-3042
      </li>
      <li>
        <svg viewBox="0 0 12 12" aria-hidden="true"><path d="M0 2h12v1L6 7 0 3zM0 4.5l6 4 6-4V10H0z"/></svg>
        publisher@vornadel-example.com
      </li>
      <li>
        <svg viewBox="0 0 12 12" aria-hidden="true"><path d="M6 0a6 6 0 1 0 0 12A6 6 0 0 0 6 0zm0 1.2c.6.6 1.1 1.8 1.3 3.3H4.7C4.9 3 5.4 1.8 6 1.2zM1.3 5.5h2.4c0 1.1.1 2.1.4 3H2A4.8 4.8 0 0 1 1.3 5.5zm3.4 0h2.6c0 1.1-.2 2.1-.5 3H5.2c-.3-.9-.5-1.9-.5-3zm3.6 0h2.4a4.8 4.8 0 0 1-.7 3H7.9c.3-.9.4-1.9.4-3z"/></svg>
        www.vornadel-example.com
      </li>
    </ul>

    <div class="address">4-237 Pellridge Street, Toronto, ON M4T 2K8</div>
  </div>
</body>
</html>
```